VelloPath Business Card

Our company is called VelloPath and we are based in Tel Aviv, Israel. We create innovative and exciting methods for getting people on the web engaged with content. We need a cool yet professional business card that will represent our management level employees. keep in mind this is a start up company with a young atmosphere. You can be inspired by our logo (file attached, make sure you have the right font "Ubuntu-Condensed") Use the colors that are used in the logo and create a colourful and professional business card.

```html
<!DOCTYPE html>
<html lang="en">
<head>
<meta charset="utf-8">
<title>VelloPath Business Card</title>
<link rel="stylesheet" href="https://fonts.googleapis.com/css2?family=Ubuntu+Condensed&family=Ubuntu:wght@400;500&display=swap">
<style>
  :root {
    --bg: #e9e6e1;
    --card: #ffffff;
    --ink: #2b2b2b;
    --blue: #3a7bbf;
    --teal: #2e86b5;
    --pink: #e8357f;
    --shadow: rgba(60, 40, 20, 0.28);
  }
  * { margin: 0; padding: 0; box-sizing: border-box; }
  html, body {
    width: 1200px;
    height: 912px;
    overflow: hidden;
    background: var(--bg);
  }
  .canvas {
    position: relative;
    width: 1200px;
    height: 912px;
  }
  .card {
    position: absolute;
    width: 560px;
    height: 320px;
    background: var(--card);
    box-shadow: 0 14px 30px var(--shadow), 0 2px 4px rgba(0,0,0,0.12);
    font-family: "Ubuntu Condensed", "Ubuntu", sans-serif;
    color: var(--ink);
  }
  .card--front { left: 70px; top: 90px; }
  .card--back { left: 570px; top: 500px; }

  /* front */
  .brand {
    position: absolute;
    left: 44px;
    top: 150px;
    display: flex;
    align-items: center;
    gap: 12px;
  }
  .brand__dot {
    width: 26px;
    height: 26px;
    border-radius: 50%;
    background: var(--pink);
  }
  .brand__name {
    font-size: 40px;
    line-height: 1;
    color: var(--ink);
  }
  .divider {
    position: absolute;
    left: 292px;
    top: 96px;
    width: 2px;
    height: 128px;
    background: var(--blue);
  }
  .contact {
    position: absolute;
    left: 316px;
    top: 96px;
    font-size: 14px;
    line-height: 18px;
  }
  .contact__name {
    font-size: 24px;
    line-height: 26px;
    color: var(--blue);
    letter-spacing: 0.5px;
    margin-bottom: 4px;
  }
  .contact__role {
    font-size: 12px;
    color: var(--ink);
    margin-left: 6px;
    letter-spacing: 0.5px;
  }
  .contact__web { color: var(--blue); }

  /* back */
  .back-brand {
    position: absolute;
    left: 0;
    right: 0;
    top: 92px;
    display: flex;
    justify-content: center;
    align-items: center;
    gap: 18px;
  }
  .back-brand__dot {
    width: 64px;
    height: 64px;
    border-radius: 50%;
    background: var(--pink);
  }
  .back-brand__name {
    font-size: 60px;
    line-height: 1;
    color: var(--ink);
  }
  .back-web {
    position: absolute;
    left: 34px;
    bottom: 28px;
    font-size: 20px;
    color: var(--teal);
    letter-spacing: 0.5px;
  }
</style>
</head>
<body>
<main class="canvas">
  <section class="card card--front" aria-label="Business card front">
    <div class="brand">
      <span class="brand__dot"></span>
      <span class="brand__name">VelloPath</span>
    </div>
    <div class="divider"></div>
    <div class="contact">
      <p class="contact__name">DANA LEVIN<span class="contact__role">DIRECTOR</span></p>
      <p>YOUR ADDRESS</p>
      <p>T +972.3.555.0142</p>
      <p>F +972.3.555.0198</p>
      <p>E dana@vellopath.com</p>
      <p class="contact__web">www.vellopath.com</p>
    </div>
  </section>

  <section class="card card--back" aria-label="Business card back">
    <div class="back-brand">
      <span class="back-brand__dot"></span>
      <span class="back-brand__name">VelloPath</span>
    </div>
    <p class="back-web">www.vellopath.com</p>
  </section>
</main>
</body>
</html>
```